I need a business card design for: Brindle Financial Solutions. Logo design has been attached. I will also need the business address: 84 West Harrow St. Suite 410C Carrow Falls, PA 16950. Phone and Fax : 555-318-0947 (phone) and 555-318-0949 (fax). Email address: tbrindle@brindlefinancialsolutions.example. Please add my title: Financial Advisor.
The following disclosure must appear on business card, letterhead, and stationary: Securities and investment advisory services offered through LPD Holdings Corporation (LPD) member QOTEB/WAHL. LPD is separately owned and other entities and/or marketing names, products or services referenced here are independent of LPD.

```html
<!DOCTYPE html>
<html lang="en">
<head>
<meta charset="utf-8">
<title>Brindle Financial Solutions – Stationery</title>
<link href="https://fonts.googleapis.com/css2?family=Open+Sans:wght@400;600&display=swap" rel="stylesheet">
<style>
:root{
  --navy:#244a78;
  --navy-light:#1f5289;
  --navy-dark:#23436c;
  --grey-band:#6e6e70;
  --paper:#f4f4f4;
  --ground:#e8e8e8;
  --ink:#4a4a4a;
  --white:#ffffff;
}
*{margin:0;padding:0;box-sizing:border-box}
html,body{width:1200px;height:795px;overflow:hidden}
body{background:var(--ground);font-family:"Open Sans",Arial,sans-serif;color:var(--ink);position:relative}
.piece{position:absolute;background:var(--paper);overflow:hidden}

.brand-name{font-family:"Open Sans",Arial,sans-serif;font-weight:600;color:var(--navy);text-transform:uppercase;line-height:1.15;text-align:center;white-space:nowrap}
.brand-name span{display:block}

.band{position:absolute;left:0;bottom:0;width:100%;display:block}
.label{font-weight:600;color:var(--navy);margin-right:1px}

/* Letterhead */
.letterhead{left:293px;top:99px;width:292px;height:414px}
.letterhead .brand-name{position:absolute;left:30px;top:47px;width:80px;font-size:7px}
.letterhead .brand-name span+span{font-size:5px;letter-spacing:2px}
.contact-block{position:absolute;left:181px;top:24px;font-size:3.6px;line-height:5px;font-weight:600;color:#555;font-style:normal;white-space:nowrap}
.contact-block .gap{margin-top:1px}
.letter-body{position:absolute;left:30px;top:104px;width:231px;font-size:5.2px;line-height:7.6px;color:#555;text-align:justify}
.letter-body p{margin-bottom:7.6px}
.disclosure{position:absolute;left:30px;top:391px;width:232px;font-size:3.6px;line-height:5px;font-weight:600;color:#666}

/* Folder */
.folder{left:637px;top:80px;width:346px;height:437px;background:linear-gradient(180deg,var(--navy-light) 0%,var(--navy-dark) 100%)}
.folder-spine{position:absolute;left:4px;top:0;width:14px;height:100%;border-left:1px solid rgba(255,255,255,.12);border-right:1px solid rgba(255,255,255,.12)}
.folder .brand-name{position:absolute;left:0;top:232px;width:100%;color:var(--white);font-size:22px}
.brand-name .folder-sub{display:flex;align-items:center;justify-content:center;gap:5px;margin-top:1px}
.folder-sub i{display:block;width:47px;height:1px;background:var(--white)}
.folder-sub b{font-weight:600;font-size:12px;letter-spacing:6px;margin-right:-6px}

/* Business cards */
.card-front{left:187px;top:551px;width:133px;height:75px;background:var(--navy)}
.card-front .brand-name{position:absolute;left:0;top:18px;width:100%;color:var(--white);font-size:7px}
.card-front .brand-name span+span{font-size:4.5px;letter-spacing:2px}
.card-front .disclosure-small{position:absolute;left:10px;top:41px;width:113px;font-size:2.9px;line-height:4.3px;color:var(--white);text-align:center;font-weight:600}

.card-back{left:187px;top:646px;width:133px;height:75px}
.card-back .brand-name{position:absolute;left:6px;top:28px;width:56px;font-size:5px}
.card-back .brand-name span+span{font-size:3.5px;letter-spacing:1.5px}
.card-divider{position:absolute;left:64px;top:22px;width:.6px;height:34px;background:var(--navy)}
.card-details{position:absolute;left:68px;top:21px;font-size:2.4px;line-height:3.4px;color:#444;font-weight:600;white-space:nowrap}
.card-details .person{font-size:3.8px;color:var(--navy);line-height:4.2px}
.card-details .title{margin-bottom:2px;font-size:2.8px}

/* Envelopes */
.envelope-front{left:353px;top:561px;width:329px;height:157px}
.envelope-front .brand-name{position:absolute;left:18px;top:44px;width:100px;font-size:8px}
.envelope-front .brand-name span+span{font-size:5px;letter-spacing:2.5px}
.envelope-address{position:absolute;left:18px;top:68px;width:100px;font-size:5px;line-height:6.6px;text-align:center;color:#444;font-style:normal}

.envelope-back{left:713px;top:561px;width:329px;height:157px}
.envelope-flap{position:absolute;left:0;top:0;width:100%;height:58px;display:block}
.envelope-back .brand-name{position:absolute;left:0;top:20px;width:100%;color:var(--white);font-size:7px}
</style>
</head>
<body>

<section class="piece letterhead" aria-label="Letterhead">
  <div class="brand-name"><span>Brindle Financial</span><span>Solutions</span></div>
  <address class="contact-block">
    <div>Brindle Financial Solutions</div>
    <div>84 West Harrow St. Suite</div>
    <div>410C Carrow Falls, PA 16950</div>
    <div class="gap"><span class="label">P</span> 555-318-0947</div>
    <div><span class="label">F</span> 555-318-0949</div>
    <div><span class="label">E</span> tbrindle@brindlefinancialsolutions.example</div>
    <div><span class="label">W</span> www.brindlefinancialsolutions.example</div>
  </address>
  <div class="letter-body">
    <p>Dear customer,</p>
    <p>Lorem ipsum dolor sit amet, consectetur adipisicing elit, sed do eiusmod tempor incididunt ut labore et dolore magna aliqua. Ut enim ad minim veniam, quis nostrud exercitation ullamco laboris nisi ut aliquip ex ea commodo consequat. Duis aute irure dolor in reprehenderit in voluptate velit esse cillum dolore eu fugiat nulla pariatur. Excepteur sint occaecat cupidatat non proident, sunt in culpa qui officia deserunt mollit anim id est laborum.</p>
    <p>Lorem ipsum dolor sit amet, consectetur adipisicing elit, sed do eiusmod tempor incididunt ut labore et dolore magna aliqua. Ut enim ad minim veniam, quis nostrud exercitation ullamco laboris nisi ut aliquip ex ea commodo consequat. Duis aute irure dolor in reprehenderit in voluptate velit esse cillum dolore eu fugiat nulla pariatur. Excepteur sint occaecat cupidatat non proident, sunt in culpa qui officia deserunt mollit anim id est laborum.</p>
    <p>Lorem ipsum dolor sit amet, consectetur adipisicing elit, sed do eiusmod tempor incididunt ut labore et dolore magna aliqua. Ut enim ad minim veniam, quis nostrud exercitation ullamco laboris nisi ut aliquip ex ea commodo consequat. Duis aute irure dolor in reprehenderit in voluptate velit esse cillum dolore eu fugiat nulla pariatur. Excepteur sint occaecat cupidatat non proident, sunt in culpa qui officia deserunt mollit anim id est laborum.</p>
    <p>Lorem ipsum dolor sit amet, consectetur adipisicing elit, sed do eiusmod tempor incididunt ut labore et dolore magna aliqua. Ut enim ad minim veniam, quis nostrud exercitation ullamco laboris nisi ut aliquip ex ea commodo consequat. Duis aute irure dolor in reprehenderit.</p>
    <p>Yours Sincerely,</p>
  </div>
  <p class="disclosure">Securities and investment advisory services offered through LPD Holdings Corporation (LPD) member QOTEB/WAHL. LPD is separately owned and other entities and/or marketing names, products or services referenced here are independent of LPD.</p>
  <svg class="band" viewBox="0 0 292 5" height="5" preserveAspectRatio="none" aria-hidden="true">
    <polygon points="0,0 197,0 193,5 0,5" fill="var(--grey-band)"/>
    <polygon points="200,0 292,0 292,5 196,5" fill="var(--navy)"/>
  </svg>
</section>

<section class="piece folder" aria-label="Presentation folder">
  <div class="folder-spine"></div>
  <div class="brand-name">
    <span>Brindle Financial</span>
    <span class="folder-sub"><i></i><b>Solutions</b><i></i></span>
  </div>
</section>

<section class="piece card-front" aria-label="Business card front">
  <div class="brand-name"><span>Brindle Financial</span><span>Solutions</span></div>
  <p class="disclosure-small">Securities and investment advisory services offered through LPD Holdings Corporation (LPD) member QOTEB/WAHL. LPD is separately owned and other entities and/or marketing names, products or services referenced here are independent of LPD.</p>
</section>

<section class="piece card-back" aria-label="Business card back">
  <div class="brand-name"><span>Brindle Financial</span><span>Solutions</span></div>
  <div class="card-divider"></div>
  <div class="card-details">
    <div class="person">DANA WHITLOW</div>
    <div class="title">Financial Advisor</div>
    <div>Brindle Financial Solutions</div>
    <div>84 West Harrow St. Suite</div>
    <div>410C Carrow Falls, PA 16950</div>
    <div><span class="label">P</span> 555-318-0947</div>
    <div><span class="label">F</span> 555-318-0949</div>
    <div><span class="label">E</span> tbrindle@brindlefinancialsolutions.example</div>
  </div>
  <svg class="band" viewBox="0 0 133 3" height="3" preserveAspectRatio="none" aria-hidden="true">
    <polygon points="0,0 81,0 79,3 0,3" fill="var(--grey-band)"/>
    <polygon points="83,0 133,0 133,3 81,3" fill="var(--navy)"/>
  </svg>
</section>

<section class="piece envelope-front" aria-label="Envelope front">
  <div class="brand-name"><span>Brindle Financial</span><span>Solutions</span></div>
  <address class="envelope-address">84 West Harrow St. Suite<br>410C Carrow Falls, PA 16950</address>
  <svg class="band" viewBox="0 0 329 6" height="6" preserveAspectRatio="none" aria-hidden="true">
    <polygon points="0,0 203,0 198,6 0,6" fill="var(--grey-band)"/>
    <polygon points="207,0 329,0 329,6 202,6" fill="var(--navy)"/>
  </svg>
</section>

<section class="piece envelope-back" aria-label="Envelope back">
  <svg class="envelope-flap" viewBox="0 0 329 58" preserveAspectRatio="none" aria-hidden="true">
    <path d="M0,0 H329 L323,50 Q322,55 316,55 H13 Q7,55 6,50 Z" fill="var(--navy)"/>
  </svg>
  <div class="brand-name"><span>Brindle Financial Solutions</span></div>
</section>

</body>
</html>
```